Graphic Design Project - FOR A SIGN

We are going to open a Cajun Restaurant. We are looking for a design for a sign. The sign is about 8' wide by about 4' to 5' tall.
The existing sign is oval shaped (shape of an eye). We're looking for a Great design that would really catch your eye as you pass by the restaurant.
It has to have a Cajun Theme. We have not even named the restaurant! Any name you come up with would be great. Cajun Bayou, Alligator Alley, Bayou Skillet, Cajun Bayou Lounge and Bar.... Cajun Food Shack and Lounge... anything you can think of.... We would like it to be "Fun".... There is a bar in the restaurant so we would possibly like that mentioned....
Thank you,
Darren Holt
dholt71@mailvero.net
317-582-6194
The Masses... Typical Blue Collar Family....
Restaurant

```html
<!DOCTYPE html>
<html lang="en">
<head>
<meta charset="utf-8">
<title>Bayou Skillet Lounge &amp; Bar – Sign</title>
<link rel="stylesheet" href="https://fonts.googleapis.com/css2?family=Questrial&family=Arimo:wght@700&display=swap">
<style>
  :root {
    --ink: #000000;
    --cajun-red: #e31e25;
    --white: #ffffff;
  }
  html, body {
    margin: 0;
    padding: 0;
    overflow: hidden;
    background: var(--ink);
  }
  .sign {
    position: relative;
    width: 1200px;
    height: 776px;
    background: var(--ink);
    overflow: hidden;
    font-family: "Questrial", "Century Gothic", sans-serif;
    color: var(--white);
  }
  .brand-mark {
    position: absolute;
    left: 62px;
    top: 62px;
    width: 230px;
    height: 230px;
    border-radius: 50%;
    background: var(--cajun-red);
  }
  .brand-name {
    position: absolute;
    left: 318px;
    top: 62px;
    width: 820px;
    margin: 0;
    font-family: "Questrial", "Century Gothic", sans-serif;
    font-weight: 400;
    font-size: 118px;
    line-height: 130px;
    color: var(--cajun-red);
    text-align: right;
    white-space: nowrap;
  }
  .brand-rule {
    position: absolute;
    left: 447px;
    top: 198px;
    width: 686px;
    height: 4px;
    background: var(--cajun-red);
  }
  .brand-tagline {
    position: absolute;
    left: 447px;
    top: 208px;
    width: 686px;
    margin: 0;
    font-family: "Arimo", Arial, sans-serif;
    font-weight: 700;
    font-size: 60px;
    line-height: 62px;
    text-align: center;
    letter-spacing: 1px;
    white-space: nowrap;
  }
  .banner {
    position: absolute;
    left: 0;
    top: 352px;
    width: 1200px;
    height: 96px;
    background: var(--cajun-red);
    border-top: 5px solid var(--white);
    border-bottom: 5px solid var(--white);
    display: flex;
    align-items: center;
    justify-content: center;
  }
  .banner-text {
    margin: 0;
    font-size: 60px;
    font-weight: 400;
    letter-spacing: 1px;
    white-space: nowrap;
  }
  .contact {
    position: absolute;
    left: 0;
    top: 528px;
    width: 1200px;
    text-align: center;
  }
  .contact p {
    margin: 0;
    white-space: nowrap;
  }
  .reserve-label {
    font-size: 38px;
    line-height: 48px;
    letter-spacing: 1px;
  }
  .reserve-phone {
    font-size: 40px;
    line-height: 48px;
    color: var(--cajun-red);
    letter-spacing: 1px;
  }
  .reach-label {
    margin-top: 26px !important;
    font-size: 34px;
    line-height: 42px;
    letter-spacing: 1px;
  }
  .reach-details {
    font-size: 26px;
    line-height: 36px;
    color: var(--cajun-red);
  }
  .reach-details .divider {
    color: var(--white);
    padding: 0 8px;
  }
</style>
</head>
<body>
  <main class="sign">
    <div class="brand-mark" role="img" aria-label="Red crawfish illustration"></div>
    <h1 class="brand-name">Bayou Skillet</h1>
    <div class="brand-rule"></div>
    <p class="brand-tagline">LOUNGE &amp; BAR</p>

    <section class="banner">
      <h2 class="banner-text">AUTHENTHIC KAJUN CUISINE</h2>
    </section>

    <section class="contact">
      <p class="reserve-label">FOR RESERVATIONS CALL US AT</p>
      <p class="reserve-phone">317-582-6194</p>
      <p class="reach-label">YOU CAN ALSO CONTACT US AT</p>
      <p class="reach-details">Cedar Bend, Indiana<span class="divider">//</span>bayouskillet.com/social<span class="divider">//</span>dholt71@mailvero.net</p>
    </section>
  </main>
</body>
</html>
```